Road Construction Company needs business cards

We would like a new business card designed for our business.

We're a road construction company based in Qld, Australia.

Can the business card please have the following information on it.

Name: Brent Malvoy
Position: General Manager
Phone: 0471 592 304
Email: Brent.malvoy@quendix.com.au
Address: 87 Harrowgate Ave, Pindarra, QLD, 4000
Website: www.quendix.com.au

Visually we'd like the card to be professional and simple.

Attached is our logo.

Our website is www.quendix.com.au

Target Market(s)

Men aged 25-60

Contact Information for Business Card

As listed in project description

Font styles to use
Serif

Requirements
Must have
• Large logo on back of card

```html
<!DOCTYPE html>
<html lang="en">
<head>
<meta charset="utf-8">
<title>Quendix Business Card</title>
<link rel="stylesheet" href="https://fonts.googleapis.com/css2?family=Lato:wght@400;900&family=Marcellus&display=swap">
<style>
  :root {
    --brand-blue: #0066b3;
    --brand-blue-dark: #0a5aa3;
    --paper: #ffffff;
    --page: #ffffff;
  }
  html, body {
    margin: 0;
    padding: 0;
    width: 1200px;
    height: 1200px;
    overflow: hidden;
    background: var(--page);
  }
  .canvas {
    position: relative;
    width: 1200px;
    height: 1200px;
  }
  .card {
    position: absolute;
    top: 480px;
    width: 419px;
    height: 240px;
    border-radius: 14px;
    box-sizing: border-box;
    overflow: hidden;
  }
  .card-front {
    left: 165px;
    background: var(--brand-blue);
  }
  .card-back {
    left: 616px;
    background: var(--paper);
    border: 1px solid var(--brand-blue);
  }
  .front-wordmark {
    position: absolute;
    left: 0;
    right: 0;
    top: 92px;
    text-align: center;
    font-family: "Lato", sans-serif;
    font-weight: 900;
    font-size: 44px;
    letter-spacing: 3px;
    color: var(--paper);
    line-height: 1;
  }
  .contact-list {
    position: absolute;
    top: 50px;
    left: 0;
    right: 0;
    margin: 0;
    padding: 0;
    list-style: none;
    text-align: center;
    font-family: "Lato", sans-serif;
    font-size: 13px;
    color: var(--brand-blue);
  }
  .contact-item {
    height: 19px;
    line-height: 19px;
  }
  .contact-icon {
    display: inline-block;
    vertical-align: -3px;
    width: 13px;
    height: 13px;
    margin-right: 8px;
  }
  .name-band {
    position: absolute;
    left: 0;
    top: 0;
    width: 419px;
    height: 240px;
  }
  .holder {
    position: absolute;
    left: 0;
    width: 198px;
    top: 172px;
    text-align: center;
    color: var(--paper);
  }
  .holder-name {
    font-family: "Marcellus", serif;
    font-size: 19px;
    line-height: 1.1;
  }
  .holder-role {
    font-family: "Marcellus", serif;
    font-size: 11px;
    line-height: 1.3;
  }
  .back-wordmark {
    position: absolute;
    right: 28px;
    top: 181px;
    font-family: "Lato", sans-serif;
    font-weight: 900;
    font-size: 22px;
    letter-spacing: 1.5px;
    color: var(--brand-blue-dark);
    line-height: 1;
  }
</style>
</head>
<body>
<main class="canvas">
  <section class="card card-front" aria-label="Card front">
    <div class="front-wordmark">QUENDIX</div>
  </section>

  <section class="card card-back" aria-label="Card back">
    <ul class="contact-list">
      <li class="contact-item">
        <svg class="contact-icon" viewBox="0 0 14 14"><rect x="0.5" y="0.5" width="13" height="13" rx="2.5" fill="none" stroke="var(--brand-blue)"/><path d="M4.3 3.6l1.4-.3.8 1.8-.9.7c.5 1 1.2 1.7 2.2 2.2l.7-.9 1.8.8-.3 1.4c-3.3.2-5.9-2.4-5.7-5.7z" fill="var(--brand-blue)"/></svg>0471 592 304
      </li>
      <li class="contact-item">
        <svg class="contact-icon" viewBox="0 0 14 14"><rect x="0.5" y="0.5" width="13" height="13" rx="2.5" fill="none" stroke="var(--brand-blue)"/><rect x="3" y="4" width="8" height="6" fill="var(--brand-blue)"/><path d="M3 4l4 3.2L11 4" fill="none" stroke="#fff" stroke-width="0.9"/></svg>Brent.malvoy@quendix.com.au
      </li>
      <li class="contact-item">
        <svg class="contact-icon" viewBox="0 0 14 14"><rect x="0.5" y="0.5" width="13" height="13" rx="2.5" fill="none" stroke="var(--brand-blue)"/><path d="M7 11.5S4 8.2 4 6a3 3 0 0 1 6 0c0 2.2-3 5.5-3 5.5z" fill="var(--brand-blue)"/><circle cx="7" cy="6" r="1.1" fill="#fff"/></svg>87 Harrowgate Ave, Pindarra, QLD, 4000
      </li>
      <li class="contact-item">
        <svg class="contact-icon" viewBox="0 0 14 14"><rect x="0.5" y="0.5" width="13" height="13" rx="2.5" fill="none" stroke="var(--brand-blue)"/><g fill="none" stroke="var(--brand-blue)" stroke-width="0.8"><circle cx="7" cy="7" r="3.6"/><ellipse cx="7" cy="7" rx="1.6" ry="3.6"/><path d="M3.4 7h7.2M3.9 5.2h6.2M3.9 8.8h6.2"/></g></svg>www.quendix.com.au
      </li>
    </ul>

    <svg class="name-band" viewBox="0 0 419 240" aria-hidden="true">
      <path d="M0 166H186Q195 166 201 173L220 210H0Z" fill="var(--brand-blue)"/>
      <line x1="218" y1="209.5" x2="419" y2="209.5" stroke="var(--brand-blue)" stroke-width="1.2"/>
    </svg>

    <div class="holder">
      <div class="holder-name">Brent Malvoy</div>
      <div class="holder-role">General Manager</div>
    </div>

    <div class="back-wordmark">QUENDIX</div>
  </section>
</main>
</body>
</html>
```